KLT Motorhaus Automotive Repair and Service Shop

I need an informative and interactive website for my automotive service and repair shop. The website must give information about the shop, as well as the ability to make bookings and a forums page for our users to use and set up an account with us, in which we can give promotions via email. We are located in Pompano Beach Florida and our company name is KLT Motorhaus. Our color scheme is a red for accent and grey (neutral color) as a base. The design must communicate our message and be able to grow should we decide to retail parts in the future. One of the websites I take the highest inspiration from is http://www.brimfieldpanelworks.com/. Although I do not have as nearly as many certifications as them. Attached are some images of our shop so you can see how clean and modern our building is, and I would like our website to match our feel. Thank you.

Target Market(s)

Automotive Enthusiasts

Industry/Entity Type

Automotive

Contact Information for Business Card

KLT Motorhaus /555 718 4062 /dorian@kltmotorhaus.com/ 612 SW 27th Ave Harlow Bay FL 32190/ any other info needed please ask me

Coding

Coded - Design and coding required

Number of Pages Required

5+ page

Font styles to use
Sans Serif

Requirements
Must have
• Name, logo, contact info, location, phone number
Nice to have
• Building is very modern, would like a business card to match
Should not have
• Not to playful or vibrant

```html
<!DOCTYPE html>
<html lang="en">
<head>
<meta charset="utf-8">
<title>KLT Motorhaus — Automotive Service</title>
<link rel="stylesheet" href="https://fonts.googleapis.com/css2?family=Oswald:wght@300;400;500;600&family=Lato:wght@400;700&display=swap">
<style>
:root{
  --red:#d81f1f;
  --ink:#1f1f1f;
  --text:#444;
  --muted:#666;
  --grey-bg:#dcdcdc;
  --grey-light:#e9e9e9;
  --panel:#3a3a3a;
  --footer:#1e1e1e;
  --footer-bottom:#151515;
  --white:#fff;
}
*{box-sizing:border-box;margin:0;padding:0}
html,body{width:1200px;height:3878px;overflow:hidden}
body{position:relative;background:var(--white);font-family:'Lato',sans-serif;color:var(--text)}
.abs{position:absolute}
.head{font-family:'Oswald',sans-serif;color:var(--ink);letter-spacing:1px}
.btn{position:absolute;background:var(--red);color:var(--white);font-family:'Lato',sans-serif;font-weight:700;display:flex;align-items:center;justify-content:center;letter-spacing:.5px}
.rule{position:absolute;height:3px;background:var(--red)}

/* header */
.site-header{position:absolute;left:0;top:0;width:1200px;height:100px;background:linear-gradient(#fff,#f1f1f1)}
.nav-link{position:absolute;top:48px;font-family:'Oswald',sans-serif;font-size:13px;font-weight:500;color:var(--ink);transform:translateX(-50%);white-space:nowrap}
.nav-link.active{color:var(--red)}
.logo-tab{position:absolute;left:455px;top:0;width:283px;height:128px;background:#f4f4f4;clip-path:polygon(0 0,100% 0,100% 84%,92% 100%,8% 100%,0 84%);box-shadow:0 2px 6px rgba(0,0,0,.2)}
.logo-name{position:absolute;left:455px;top:20px;width:283px;text-align:center;font-family:'Oswald',sans-serif;font-weight:600;font-size:25px;color:var(--ink)}
.logo-square{position:absolute;left:582px;top:66px;width:30px;height:30px;background:var(--red)}
.auth{position:absolute;top:39px;height:32px;font-family:'Oswald',sans-serif;font-size:13px;font-weight:500;display:flex;align-items:center;justify-content:center;border:2px solid}
.auth.login{left:1003px;width:78px;color:var(--red);border-color:var(--red)}
.auth.signup{left:1090px;width:78px;color:var(--ink);border-color:var(--ink)}

/* hero */
.hero{position:absolute;left:0;top:100px;width:1200px;height:603px;background:radial-gradient(ellipse at 70% 55%,#c98a16 0%,#6a4b17 18%,#1d3555 45%,#0e1c33 100%)}
.hero-kicker{position:absolute;left:136px;top:266px;font-family:'Oswald',sans-serif;font-weight:300;font-size:44px;line-height:56px;color:var(--white);letter-spacing:2px}
.hero-title{position:absolute;left:136px;top:314px;font-family:'Oswald',sans-serif;font-weight:500;font-size:50px;line-height:62px;color:var(--white);letter-spacing:1px}
.hero-copy{position:absolute;left:138px;top:382px;font-size:16.5px;line-height:32px;color:var(--white)}
.dot{position:absolute;left:55px;width:10px;height:10px;border-radius:50%;background:var(--white)}
.dot.ring{background:transparent;border:2px solid var(--white)}

/* services */
.services{position:absolute;left:0;top:703px;width:1200px;height:477px;background:var(--grey-bg)}
.section-title{position:absolute;left:0;width:1200px;text-align:center;font-family:'Oswald',sans-serif;font-weight:500;color:var(--ink);letter-spacing:1.5px}
.service-card{position:absolute;width:255px;height:267px}
.service-card span{position:absolute;left:0;bottom:16px;width:100%;text-align:center;font-weight:700;font-size:17px;color:var(--white)}

/* about */
.about-photo{position:absolute;left:0;top:1180px;width:630px;height:493px;background:linear-gradient(120deg,#3a3d42 0%,#6d6a66 45%,#2d4b66 100%);clip-path:polygon(0 0,516px 0,630px 50%,516px 100%,0 100%)}
.about-copy{position:absolute;left:676px;font-size:13.5px;line-height:22px;color:var(--text);width:430px}

/* testimonials */
.testimonials{position:absolute;left:0;top:1673px;width:1200px;height:435px;background:linear-gradient(#cfcfcf,#c4c4c4)}
.quote-card{position:absolute;top:1823px;width:299px;height:208px;background:var(--white);border:1px solid #bbb}
.stars{position:absolute;left:36px;top:34px;display:flex;gap:3px}
.quote-text{position:absolute;left:36px;top:64px;width:240px;font-size:14px;line-height:22.5px;color:var(--muted)}
.quote-author{position:absolute;left:36px;top:146px;font-size:14px;color:#333}
.quote-city{position:absolute;left:36px;top:166px;font-size:11px;color:var(--muted)}

/* booking */
.booking-photo{position:absolute;left:450px;top:2182px;width:617px;height:408px;background:linear-gradient(110deg,#5a5e63 0%,#27467a 40%,#8a8f96 70%,#c9c3bf 100%)}
.booking-frame{position:absolute;left:113px;top:2225px;width:490px;height:322px;border:1.5px solid var(--red)}
.booking-panel{position:absolute;left:122px;top:2234px;width:473px;height:304px;background:var(--panel)}
.booking-copy{position:absolute;left:122px;width:473px;text-align:center;color:var(--white);font-size:13.5px;font-weight:700;line-height:21px}

/* newsletter */
.newsletter{position:absolute;left:0;top:2653px;width:1200px;height:337px;background:linear-gradient(160deg,#2c2c2c 0%,#555 40%,#3a3a3a 60%,#1e1e1e 100%)}
.email-field{position:absolute;left:334px;top:2831px;width:359px;height:45px;background:var(--white);font-size:13px;color:#333;display:flex;align-items:center;padding-left:22px}

/* blogs */
.blogs{position:absolute;left:0;top:2990px;width:1200px;height:536px;background:var(--grey-light)}
.blog-photo{position:absolute;top:3101px;width:305px;height:192px}
.blog-title{position:absolute;top:3310px;width:310px;font-size:20px;line-height:27px;color:var(--ink);font-weight:700}
.blog-copy{position:absolute;top:3373px;width:300px;font-size:12px;line-height:18px;color:var(--muted)}
.read-more{position:absolute;top:3423px;font-size:13px;font-weight:700;color:var(--ink)}
.read-more::after{content:"";position:absolute;left:0;top:22px;width:28px;height:3px;background:var(--red)}

/* footer */
.site-footer{position:absolute;left:0;top:3526px;width:1200px;height:292px;background:var(--footer)}
.footer-bottom{position:absolute;left:0;top:3818px;width:1200px;height:60px;background:var(--footer-bottom);color:#888;font-size:11px;display:flex;align-items:center;justify-content:center}
.footer-col{position:absolute;top:3585px}
.footer-col h4{font-family:'Oswald',sans-serif;font-weight:400;font-size:18px;color:var(--white);margin-bottom:9px}
.footer-col li{list-style:none;font-size:12px;color:#ddd;line-height:25.6px}
.contact-line{display:flex;align-items:center;gap:8px;font-size:12px;color:#ddd;line-height:21px;white-space:nowrap}
.social{position:absolute;width:32px;height:32px;border-radius:50%;border:1.5px solid var(--white)}
.social.accent{border-color:var(--red)}
</style>
</head>
<body>

<header class="site-header">
  <a class="nav-link active" style="left:119px">HOME</a>
  <a class="nav-link" style="left:209px">ABOUT US</a>
  <a class="nav-link" style="left:309px">SERVICES</a>
  <a class="nav-link" style="left:400px">FORUM</a>
  <a class="nav-link" style="left:765px">BOOKING</a>
  <a class="nav-link" style="left:854px">BLOGS</a>
  <a class="nav-link" style="left:944px">CONTACT</a>
  <div class="auth login">LOGIN</div>
  <div class="auth signup">SIGN UP</div>
</header>

<section class="hero" role="img" aria-label="Close-up of an engine's pistons splashed with golden oil"></section>
<div class="logo-tab"></div>
<div class="logo-name">KLT MOTORHAUS</div>
<div class="logo-square"></div>
<div class="dot ring" style="top:340px"></div>
<div class="dot" style="top:357px"></div>
<div class="dot" style="top:374px"></div>
<div class="dot" style="top:391px"></div>
<div class="hero-kicker">KLT MOTORHAUS</div>
<h1 class="hero-title">AUTOMOTIVE SERVICE</h1>
<p class="hero-copy">Aendrerit quis leo Pellentesque rutrum malesuada neque<br>Nunc tempus felis vitae urna Vivamus</p>
<div class="btn" style="left:137px;top:467px;width:178px;height:52px;font-size:16px">LEARN MORE</div>

<section class="services"></section>
<h2 class="section-title" style="top:738px;font-size:34px">OUR SERVICES</h2>
<div class="rule" style="left:573px;top:789px;width:54px"></div>
<div class="service-card" style="left:87px;top:852px;background:linear-gradient(#4d5a6e,#20252e)" role="img" aria-label="Engine block in a workshop"><span>ENGINE REPAIR</span></div>
<div class="service-card" style="left:346px;top:823px;background:linear-gradient(#bfc3c7,#3a3c40 55%,#1c1d20)" role="img" aria-label="Laptop diagnostics beside an open engine bay"><span>AUTO REPAIR</span></div>
<div class="service-card" style="left:605px;top:852px;background:linear-gradient(110deg,#2a2e35,#3d5c8f 70%,#cfd3d8)" role="img" aria-label="Mechanic with clipboard beside a car"><span>SERVICING</span></div>
<div class="service-card" style="left:863px;top:823px;background:linear-gradient(#2b4f9a,#1b2436)" role="img" aria-label="Gloved hands working on a car battery"><span>BATTERY SERVICE</span></div>

<div class="about-photo" role="img" aria-label="Mechanic working on an engine block"></div>
<h2 class="head abs" style="left:676px;top:1274px;font-size:32px;font-weight:500">ABOUT KLT MOTORHAUS</h2>
<div class="rule" style="left:677px;top:1323px;width:52px"></div>
<p class="about-copy" style="top:1349px">Augiat in pede Fusce tellus Sed metus augue convallis et vehicula ut pulvinar eu ante Integer orci tell</p>
<p class="about-copy" style="top:1412px">Morbi eget arcurmentum vel congue id euismod in elit Fusce ultricies orci ac feugiat suscipit leo massa sodales velit et scelerisque mi tortor at ipsum Proin orci odio commodo ac gravida non tristique vel te Curabitur iaculis tempus eros Curabitur vel mi sit</p>
<div class="btn" style="left:679px;top:1530px;width:155px;height:39px;font-size:13.5px">LEARN MORE</div>

<section class="testimonials" role="img" aria-label="Faint pistons on a light grey backdrop"></section>
<h2 class="section-title" style="top:1736px;font-size:28px">TESTIMONIALS</h2>
<div class="rule" style="left:573px;top:1785px;width:54px"></div>
<svg class="abs" style="left:94px;top:1906px" width="20" height="30" viewBox="0 0 20 30"><path d="M15 3 L5 15 L15 27" fill="none" stroke="#555" stroke-width="4"/></svg>
<svg class="abs" style="left:1077px;top:1906px" width="20" height="30" viewBox="0 0 20 30"><path d="M5 3 L15 15 L5 27" fill="none" stroke="#555" stroke-width="4"/></svg>

<div class="quote-card" style="left:132px">
  <div class="stars">
    <svg width="96" height="16" viewBox="0 0 96 16"><g fill="#ee5a1c"><path id="st" d="M8 0 L10 5.6 L16 5.8 L11.2 9.4 L13 15.4 L8 11.8 L3 15.4 L4.8 9.4 L0 5.8 L6 5.6Z"/><use href="#st" x="20"/><use href="#st" x="40"/><use href="#st" x="60"/><use href="#st" x="80"/></g></svg>
  </div>
  <p class="quote-text">Ante Morbi eget arcurmentum vel congue id euismod in elit Fusce ultricies orci ac feugiat</p>
  <p class="quote-author">By Author Name</p>
  <p class="quote-city">Location City</p>
</div>
<div class="quote-card" style="left:446px">
  <div class="stars"><svg width="96" height="16" viewBox="0 0 96 16"><g fill="#ee5a1c"><use href="#st"/><use href="#st" x="20"/><use href="#st" x="40"/><use href="#st" x="60"/><use href="#st" x="80"/></g></svg></div>
  <p class="quote-text">Ante Morbi eget arcurmentum vel congue id euismod in elit Fusce ultricies orci ac feugiat</p>
  <p class="quote-author">By Author Name</p>
  <p class="quote-city">Location City</p>
</div>
<div class="quote-card" style="left:757px">
  <div class="stars"><svg width="96" height="16" viewBox="0 0 96 16"><g fill="#ee5a1c"><use href="#st"/><use href="#st" x="20"/><use href="#st" x="40"/><use href="#st" x="60"/><use href="#st" x="80"/></g></svg></div>
  <p class="quote-text">Ante Morbi eget arcurmentum vel congue id euismod in elit Fusce ultricies orci ac feugiat</p>
  <p class="quote-author">By Author Name</p>
  <p class="quote-city">Location City</p>
</div>

<div class="booking-photo" role="img" aria-label="Mechanic and customer talking in the service bay"></div>
<div class="booking-frame"></div>
<div class="booking-panel"></div>
<h2 class="abs" style="left:122px;top:2280px;width:473px;text-align:center;font-family:'Oswald',sans-serif;font-weight:400;font-size:33px;color:var(--white);letter-spacing:2px">BOOKING NOW</h2>
<p class="booking-copy" style="top:2336px">Fusce tellus Sed metus augue convallis et vehicula ut<br>pulvinar eu ante Integer orci tellus tristique<br>Aitae consequat nec porta vel lectus</p>
<p class="booking-copy" style="top:2418px;font-size:16px;font-weight:400;display:flex;justify-content:center;align-items:center;gap:4px">
  <svg width="15" height="15" viewBox="0 0 24 24"><path fill="#fff" d="M6.6 10.8a15.1 15.1 0 0 0 6.6 6.6l2.2-2.2c.3-.3.7-.4 1-.2 1.1.4 2.3.6 3.6.6.6 0 1 .4 1 1V20c0 .6-.4 1-1 1A17 17 0 0 1 3 4c0-.6.4-1 1-1h3.5c.6 0 1 .4 1 1 0 1.3.2 2.5.6 3.6.1.3 0 .7-.2 1z"/></svg>
  Call Us at 800-555-0148</p>
<div class="btn" style="left:274px;top:2460px;width:172px;height:39px;font-size:14px;font-weight:400">BOOK NOW</div>

<section class="newsletter" role="img" aria-label="Aerial view of a coastline in dark monochrome"></section>
<h2 class="abs" style="left:0;top:2732px;width:1200px;text-align:center;font-family:'Oswald',sans-serif;font-weight:400;font-size:38px;color:var(--white);letter-spacing:2px">SIGN UP OUR NEWSLETTER</h2>
<p class="abs" style="left:0;top:2784px;width:1200px;text-align:center;font-size:19px;color:var(--white)">Lorem ipsum dolor sit amet consectetuer adipiscing elit Nam</p>
<div class="email-field">Email address</div>
<div class="btn" style="left:699px;top:2831px;width:162px;height:45px;font-size:16px;font-weight:400">SUBSCRIBE</div>

<section class="blogs"></section>
<h2 class="head abs" style="left:121px;top:3034px;font-size:34px;font-weight:500;letter-spacing:.5px">LATEST BLOGS</h2>

<div class="blog-photo" style="left:120px;background:linear-gradient(135deg,#cfd2d6,#4a4c50 50%,#1f2023)" role="img" aria-label="Hands working under a car bonnet"></div>
<h3 class="blog-title" style="left:122px">Augiat in pede Fusce tellus<br>Sed metus augue</h3>
<p class="blog-copy" style="left:122px">Curabitur vel dolor ultrices ipsum dictum tristique Praesent vitae lacus Ut velit enim</p>
<span class="read-more" style="left:121px">READ MORE</span>

<div class="blog-photo" style="left:467px;background:linear-gradient(135deg,#2c3440,#8a5a35 45%,#2a3a5c)" role="img" aria-label="Mechanic working on an engine part"></div>
<h3 class="blog-title" style="left:469px">Fusce tellus Sed metus augue con-<br>vallis et vehicula</h3>
<p class="blog-copy" style="left:469px">Curabitur vel dolor ultrices ipsum dictum tristique Praesent vitae lacus Ut velit enim</p>
<span class="read-more" style="left:468px">READ MORE</span>

<div class="blog-photo" style="left:813px;background:linear-gradient(135deg,#f4e2c2,#c9a26a 40%,#6f6a66)" role="img" aria-label="Car raised on a lift in a bright garage"></div>
<h3 class="blog-title" style="left:816px">Nullam enim leo egestas<br>condimentum at laor</h3>
<p class="blog-copy" style="left:816px">Curabitur vel dolor ultrices ipsum dictum tristique Praesent vitae lacus Ut velit enim</p>
<span class="read-more" style="left:815px">READ MORE</span>

<footer class="site-footer"></footer>
<div class="footer-col" style="left:161px"><h4>QUICK LINKS</h4><ul><li>Home</li><li>About us</li><li>Services</li><li>Booking</li><li>Testimonials</li></ul></div>
<div class="footer-col" style="left:332px"><h4>RESOURCES</h4><ul><li>News</li><li>Blogs</li><li>Forum</li><li>Contact Us</li></ul></div>
<div class="footer-col" style="left:488px"><h4>LINKS</h4><ul><li>Support</li><li>FAQ</li><li>Privacy Policy</li><li>Terms of Use</li></ul></div>
<div class="footer-col" style="left:669px">
  <h4>CONTACT US</h4>
  <p class="contact-line" style="font-weight:700;color:var(--white)">KLT Motorhaus</p>
  <p class="contact-line"><svg width="12" height="14" viewBox="0 0 12 16"><path fill="#d81f1f" d="M6 0a6 6 0 0 0-6 6c0 4.5 6 10 6 10s6-5.5 6-10a6 6 0 0 0-6-6zm0 8.5A2.5 2.5 0 1 1 6 3.5a2.5 2.5 0 0 1 0 5z"/></svg>612 SW 27th Ave Harlow</p>
  <p class="contact-line" style="padding-left:20px">Bay FL 32190</p>
  <p class="contact-line"><svg width="12" height="12" viewBox="0 0 24 24"><path fill="#d81f1f" d="M6.6 10.8a15.1 15.1 0 0 0 6.6 6.6l2.2-2.2c.3-.3.7-.4 1-.2 1.1.4 2.3.6 3.6.6.6 0 1 .4 1 1V20c0 .6-.4 1-1 1A17 17 0 0 1 3 4c0-.6.4-1 1-1h3.5c.6 0 1 .4 1 1 0 1.3.2 2.5.6 3.6.1.3 0 .7-.2 1z"/></svg>555 718 4062</p>
  <p class="contact-line"><svg width="13" height="10" viewBox="0 0 13 10"><rect width="13" height="10" fill="#d81f1f"/><path d="M0 0 L6.5 5.5 L13 0" fill="none" stroke="#1e1e1e" stroke-width="1.2"/></svg>dorian@kltmotorhaus.com</p>
</div>
<div class="footer-col" style="left:913px"><h4>FOLLOW US</h4></div>
<div class="social accent" style="left:916px;top:3623px"></div>
<div class="social" style="left:955px;top:3623px"></div>
<div class="social" style="left:995px;top:3623px"></div>
<div class="social" style="left:916px;top:3667px"></div>
<div class="social" style="left:955px;top:3667px"></div>
<div class="social" style="left:995px;top:3667px"></div>
<div class="footer-bottom">© 2020 Company Name | All Rights Reserved | Disclaimer</div>

</body>
</html>
```